International Firefighter Competition Needs New Website that Looks Like It's a Global Sportin...

The Blazeguard Relay is held globally and sees thousands of firefighters competing on an obstacle course known as the toughest two minutes in sports. This year the organization received a makeover with new logo and new look of our challenge course. We also introduced the Blazeguard Relay Circuit (known as the BRC). We envision a new website that inspires our next generation of competitors! It's time to wow them visually and to make them feel that this exciting sport proudly represents them as our global heroes that protect each and every one of us in a moments notice! NOTE: Photos provided are just for you to use as placeholders. TO SEE A VIDEO OF OUR EVENT: https://clipvault-example.net/734205918

NOTE: In 2023 we sub-divided the U.S. into 5 new regions for the BRC: Blazeguard Relay Circuit. I've now added these logos in the event a designer sees a vision of integrating these.

Target Market(s)

Firefighters and Sponsors

Coding

Coded - Design and coding required

Requirements
Must have
• Rival other major sporting event websites. See attached samples.
Nice to have
• No suggestions. We truly are open to creativity.
Should not have
• Too firefighter looking. Needs to be the perfect blend of promoting our firefighters as athletes in our sport.

```html
<!DOCTYPE html>
<html lang="en">
<head>
<meta charset="UTF-8">
<title>Blazeguard Relay</title>
<link rel="stylesheet" href="https://fonts.googleapis.com/css2?family=Oswald:wght@300;400;500;700&display=swap">
<style>
  :root {
    --navy: #13283f;
    --nav-band: rgba(16, 36, 58, 0.82);
    --blue: #1f9ae0;
    --red: #d8343d;
    --white: #ffffff;
    --ink: #3a3f47;
    --teal-light: #6fa4b2;
    --teal-mid: #2f6b7c;
    --teal-dark: #17333f;
    --ember: #8a5a22;
  }
  * { box-sizing: border-box; margin: 0; padding: 0; }
  html, body { width: 1200px; height: 749px; overflow: hidden; background: var(--white); }
  .page { position: relative; width: 1200px; height: 749px; overflow: hidden; font-family: 'Oswald', sans-serif; }

  .hero-photo {
    position: absolute; inset: 0 0 auto 0; height: 654px;
    background:
      radial-gradient(ellipse 380px 260px at 880px 420px, rgba(138, 90, 34, 0.75), transparent 70%),
      radial-gradient(ellipse 420px 200px at 260px 220px, rgba(200, 225, 232, 0.55), transparent 70%),
      linear-gradient(120deg, var(--teal-light) 0%, var(--teal-mid) 45%, var(--teal-dark) 100%);
    clip-path: polygon(0 0, 1200px 0, 1200px 517px, 600px 653px, 0 517px);
  }
  .wedges { position: absolute; left: 0; top: 0; width: 1200px; height: 749px; pointer-events: none; }

  .nav-band {
    position: absolute; left: 0; top: 62px; width: 1200px; height: 63px;
    background: var(--nav-band);
  }
  .social { position: absolute; left: 122px; top: 62px; height: 63px; display: flex; align-items: center; gap: 7px; }
  .social span { color: var(--white); font-size: 10px; font-weight: 500; letter-spacing: 0.3px; }

  .nav-link {
    position: absolute; top: 62px; height: 63px; line-height: 63px;
    color: var(--white); font-size: 15px; font-weight: 500; text-decoration: none; letter-spacing: 0.2px;
  }
  .nav-link.is-active::after {
    content: ""; position: absolute; left: -2px; right: 0; bottom: 0; height: 3px; background: var(--blue);
  }

  .brand-mark {
    position: absolute; left: 531px; top: 30px; width: 138px; height: 130px;
    background: var(--navy);
    display: flex; align-items: center; justify-content: center; text-align: center;
    color: var(--white); font-size: 22px; font-weight: 700; line-height: 1.05; text-transform: uppercase;
  }

  .call { position: absolute; left: 975px; top: 80px; display: flex; align-items: center; gap: 10px;
    color: var(--red); font-size: 16px; font-weight: 500; }

  .hero-title {
    position: absolute; left: 252px; top: 240px;
    color: var(--white); font-size: 58px; font-weight: 700; font-style: italic;
    line-height: 61px; letter-spacing: -0.5px; text-transform: uppercase;
  }
  .hero-text {
    position: absolute; left: 254px; top: 381px; width: 300px;
    color: var(--white); font-family: Arial, Helvetica, sans-serif; font-size: 15px; line-height: 18.5px;
  }
  .cta {
    position: absolute; left: 254px; top: 445px; width: 148px; height: 42px;
    border: 2px solid var(--white); background: var(--blue); overflow: hidden;
    color: var(--white); text-decoration: none;
  }
  .cta-label { position: absolute; left: 14px; top: 0; line-height: 38px; font-size: 18px; font-weight: 500; }
  .cta-arrow { position: absolute; left: 100px; top: 0; width: 46px; height: 38px;
    background: var(--red); clip-path: polygon(8px 0, 100% 0, 100% 100%, 0 100%); }
  .cta-arrow svg { position: absolute; left: 14px; top: 10px; }

  .footer-video { position: absolute; left: 150px; top: 691px; display: flex; align-items: center; gap: 8px;
    color: var(--ink); font-size: 14px; font-weight: 300; text-decoration: none; }
  .footer-video .dot { width: 27px; height: 19px; background: var(--red); border-radius: 4px; }
  .copyright { position: absolute; left: 0; width: 1200px; top: 695px; text-align: center;
    color: var(--ink); font-size: 14px; font-weight: 300; }
  .circuit-mark { position: absolute; left: 970px; top: 674px; width: 78px; height: 50px;
    display: flex; align-items: center; justify-content: center; background: var(--blue);
    border-radius: 5px; color: var(--white); font-size: 20px; font-weight: 700; }
</style>
</head>
<body>
<main class="page">
  <div class="hero-photo" role="img" aria-label="Photo of two firefighters in turnout gear and breathing tanks spraying a hose through mist, red and white bollards on the left"></div>

  <svg class="wedges" viewBox="0 0 1200 749" aria-hidden="true">
    <polygon points="0,517 600,653 0,574" fill="var(--blue)"/>
    <polygon points="1200,517 600,653 1200,569" fill="var(--red)"/>
  </svg>

  <header>
    <div class="nav-band"></div>
    <div class="social">
      <span>Chirp</span><span>Mesh</span><span>Wall</span>
    </div>
    <nav>
      <a class="nav-link is-active" href="#" style="left:256px">HOME</a>
      <a class="nav-link" href="#" style="left:322px">ABOUT US</a>
      <a class="nav-link" href="#" style="left:415px">OUR EVENTS</a>
      <a class="nav-link" href="#" style="left:722px">TRAINING</a>
      <a class="nav-link" href="#" style="left:809px">NEWS</a>
      <a class="nav-link" href="#" style="left:874px">CONTACT</a>
    </nav>
    <div class="brand-mark">Blazeguard<br>Relay</div>
    <div class="call">
      <svg width="14" height="14" viewBox="0 0 24 24" aria-hidden="true">
        <path fill="var(--red)" d="M6.6 10.8a15.1 15.1 0 0 0 6.6 6.6l2.2-2.2c.3-.3.7-.4 1-.2 1.1.4 2.3.6 3.6.6.6 0 1 .4 1 1V20c0 .6-.4 1-1 1A17 17 0 0 1 3 4c0-.6.4-1 1-1h3.5c.6 0 1 .4 1 1 0 1.3.2 2.5.6 3.6.1.3 0 .7-.2 1z"/>
      </svg>
      <span>CALL: 123 456 7890</span>
    </div>
  </header>

  <section class="hero">
    <h1 class="hero-title">Blazeguard<br>Relay</h1>
    <p class="hero-text">Lorem ipsum dolor sit amet, consectetur adipiscing elit, sed do eiusmod temp.</p>
    <a class="cta" href="https://clipvault-example.net/734205918">
      <span class="cta-label">OUR EVENTS</span>
      <span class="cta-arrow">
        <svg width="22" height="18" viewBox="0 0 22 18" aria-hidden="true">
          <path d="M1 9h17M11 2l7 7-7 7" stroke="var(--white)" stroke-width="3" fill="none" stroke-linecap="round" stroke-linejoin="round"/>
        </svg>
      </span>
    </a>
  </section>

  <footer>
    <a class="footer-video" href="https://clipvault-example.net/734205918"><span class="dot"></span>OUR EVENTS</a>
    <p class="copyright">COPYRIGHT © 2023 ALL RIGHTS RESERVED.</p>
    <div class="circuit-mark">BRC</div>
  </footer>
</main>
</body>
</html>
```